Accounting Practice Business Card Design

I have a logo I am happy for you to use in the design of the Business Card.
You can edit and change colours as you please, I am not fixated on it.
I am looking for a modern and clean overall feel for the finished design.

The business is a small accounting practice who thrives on word of mouth referrals and this card will be given to all current and prospect clients.

Industry/Entity Type

Accountant

Contact Information for Business Card

Marcus Elwin
Level 5, 8 Corvale Ridge Road
ASHGROVE RISE VIC 3187
Phone: 9481 3057
Email: melwin@mrfaccountants.com.au
Web: www.mrfaccountants.com.au

Font styles to use
Serif
Sans Serif

Colors
0555a3
3277b5
85acd3
0393ce
33a6d7
85cae6
00a990
33b8a4
9bcb3c

Requirements
Must have
• "The end to your tax problems begin with us"
• "A referral from you is our greatest compliment"
Nice to have
• Modern clean professional

```html
<!DOCTYPE html>
<html lang="en">
<head>
<meta charset="utf-8">
<title>MRF Accountants – Business Card</title>
<link rel="stylesheet" href="https://fonts.googleapis.com/css2?family=Oswald:wght@400;600&family=Sorts+Mill+Goudy&display=swap">
<style>
  :root {
    --stage: #9d9b9c;
    --card: #000000;
    --brand-blue: #14487f;
    --band-blue: #0555a3;
    --brand-green: #2f6b36;
    --ghost: #0c0c0c;
    --rule: #2a2a2a;
    --text-light: #b9b9b9;
    --icon-blue: #3277b5;
  }
  * { margin: 0; padding: 0; box-sizing: border-box; }
  html, body {
    width: 1025px; height: 1200px; overflow: hidden;
    background: var(--stage);
  }
  .canvas { position: relative; width: 1025px; height: 1200px; }
  .card {
    position: absolute; left: 92px; width: 840px; height: 480px;
    background: var(--card); overflow: hidden;
  }
  .card--front { top: 59px; }
  .card--back { top: 646px; }
  .card__band {
    position: absolute; left: 0; right: 0; bottom: 0; height: 10px;
    background: var(--band-blue);
  }
  .wordmark {
    position: absolute; left: 0; right: 0; text-align: center;
    font-family: "Oswald", sans-serif; font-weight: 600;
    color: var(--brand-blue); letter-spacing: 2px; line-height: 1;
  }
  .card--front .wordmark { top: 190px; font-size: 64px; }
  .card--back .wordmark { top: 100px; font-size: 60px; }
  .wordmark__sub {
    display: block; font-size: 0.42em; letter-spacing: 6px; margin-top: 10px;
  }
  .ghost-mark {
    position: absolute; left: 60px; top: -20px;
    font-family: "Oswald", sans-serif; font-weight: 600;
    font-size: 300px; line-height: 1; letter-spacing: 10px;
    color: var(--ghost);
  }
  .divider { position: absolute; left: 65px; top: 311px; width: 720px; height: 10px; }
  .contact-person { position: absolute; left: 60px; top: 348px; }
  .contact-person__name {
    font-family: "Oswald", sans-serif; font-weight: 400;
    font-size: 38px; line-height: 1; color: var(--brand-blue);
  }
  .contact-person__address {
    margin-top: 8px;
    font-family: "Sorts Mill Goudy", serif; font-size: 21px; line-height: 29px;
    color: var(--text-light);
  }
  .contact-links {
    position: absolute; right: 50px; top: 352px; list-style: none;
    font-family: "Sorts Mill Goudy", serif; color: var(--text-light);
    text-align: right;
  }
  .contact-links li {
    display: flex; justify-content: flex-end; align-items: center; gap: 8px;
    height: 30px; font-size: 20px; letter-spacing: 1px;
  }
  .contact-links li.phone { font-size: 19px; letter-spacing: 0.5px; }
  .contact-links svg { width: 18px; height: 18px; flex: none; }
</style>
</head>
<body>
<div class="canvas">

  <section class="card card--front">
    <div class="wordmark">MRF<span class="wordmark__sub">ACCOUNTANTS</span></div>
    <div class="card__band"></div>
  </section>

  <section class="card card--back">
    <div class="ghost-mark" aria-hidden="true">MRF</div>
    <div class="wordmark">MRF<span class="wordmark__sub">ACCOUNTANTS</span></div>

    <svg class="divider" viewBox="0 0 720 10" aria-hidden="true">
      <line x1="5" y1="5" x2="715" y2="5" stroke="var(--rule)" stroke-width="2"/>
      <circle cx="5" cy="5" r="5" fill="#333"/>
      <circle cx="715" cy="5" r="5" fill="#333"/>
    </svg>

    <div class="contact-person">
      <h1 class="contact-person__name">Marcus Elwin</h1>
      <p class="contact-person__address">Level 5, 8 Corvale Ridge Road<br>Ashgrove Rise vic 3187</p>
    </div>

    <ul class="contact-links">
      <li class="phone">9481 3057
        <svg viewBox="0 0 20 20" aria-hidden="true"><circle cx="10" cy="10" r="8.5" fill="none" stroke="var(--icon-blue)" stroke-width="1.3"/><path d="M7 5.5l1.6 2.2-1 1.2c.7 1.5 1.8 2.6 3.3 3.3l1.2-1 2.2 1.6-.9 1.6c-3.8-.3-6.9-3.4-7.2-7.2z" fill="none" stroke="var(--icon-blue)" stroke-width="1.1"/></svg>
      </li>
      <li>melwin@mrfaccountants.com.au
        <svg viewBox="0 0 20 20" aria-hidden="true"><circle cx="10" cy="10" r="8.5" fill="none" stroke="var(--icon-blue)" stroke-width="1.3"/><rect x="5.5" y="7" width="9" height="6.5" fill="none" stroke="var(--icon-blue)" stroke-width="1.1"/><path d="M5.5 7l4.5 3.5L14.5 7" fill="none" stroke="var(--icon-blue)" stroke-width="1.1"/></svg>
      </li>
      <li>www.mrfaccountants.com.au
        <svg viewBox="0 0 20 20" aria-hidden="true"><circle cx="10" cy="10" r="8.5" fill="none" stroke="var(--icon-blue)" stroke-width="1.3"/><ellipse cx="10" cy="10" rx="3.3" ry="8.5" fill="none" stroke="var(--icon-blue)" stroke-width="1"/><path d="M1.5 10h17M3 6h14M3 14h14" stroke="var(--icon-blue)" stroke-width="1"/></svg>
      </li>
    </ul>
  </section>

</div>
</body>
</html>
```